Design a WordPress website for a Wedding Company in Paradise

Seeking beautiful and creative WordPress website design for the Caribbean's leading small weddings and elopements firm. We have beautiful weddings (100+ a year), beautiful images, drone photos and videos, and much more, and we need a beautiful website to reflect that.

We like (not love) our current website, www.velmorangatherings.com. Much of the tabs and functionality can stay the same; however, we need a cleaner, crisper design that doesn't have glitches (yes, that's the responsibility of the coder in the future).

Featuring images and videos are very important. In addition, having a clean and elegant interface and aesthetic will allow the photos and imagery to shine.
Updates

Hi Designers, I'm so sorry but we haven't given this the attention it deserves, as our operations manager has been out of the office. We're pushing the deadline out a few days so that we can provide better and more detailed feedback for the submissions you've worked on, creating better results. Thank you for your patience!

Target Market(s)

Couples from the USA looking to travel to and get married in Puerto Rico, a beautiful Caribbean island.

Number of Pages Required

5+ page

Font styles to use
Other font styles liked:
• Fonts and colors are mostly provided in design guidelines. A versatile script font that's not too frilly might be useful as well.

Requirements
Must have
• -Clean and elegant web design. less is more.
-Utilize existing logo and colors
-Highlight photos and videos throughout
-Blog page design
-Video page design
-Photo gallery page design
-Landing page design for Zentro Clicklane campaigns
Should not have
• -lots of frills, hearts, palm trees, and stereotypical wedding and island imagery and themes

```html
<!DOCTYPE html>
<html lang="en">
<head>
<meta charset="utf-8">
<title>Featured Weddings – Velmoran Gatherings</title>
<link rel="stylesheet" href="https://fonts.googleapis.com/css2?family=Gelasio:wght@400&family=Lato:wght@400;700&display=swap">
<style>
:root{
  --gold:#dfbd78;
  --teal:#3bb3a0;
  --ink:#1f1f1f;
  --body:#6a6a6a;
  --rule:#d8d8d8;
  --white:#ffffff;
}
*{box-sizing:border-box;margin:0;padding:0}
html,body{width:1200px;height:3706px;overflow:hidden;background:var(--white)}
body{position:relative;font-family:"Lato",Arial,sans-serif;color:var(--body)}
.nav-band{position:absolute;top:125px;left:0;width:1200px;height:43px;background:var(--gold)}
.nav-link{position:absolute;top:137px;color:var(--white);font-weight:700;font-size:17px;letter-spacing:.3px;text-decoration:none}
.brand-cap{position:absolute;top:0;left:0;width:1200px;height:200px;z-index:2}
.brand{position:absolute;z-index:3;top:60px;left:0;width:1200px;text-align:center;font-family:"Gelasio",Georgia,serif;color:var(--gold);font-size:30px;line-height:1.1}
.brand-dot{position:absolute;z-index:3;top:14px;left:580px;width:40px;height:40px;border-radius:50%;background:var(--gold)}
.hero{position:absolute;top:168px;left:0;width:1200px;height:516px;background:linear-gradient(180deg,#9fb7c8 0%,#5f8aa6 38%,#b9a78f 62%,#5b5450 100%)}
.hero-title{position:absolute;top:222px;left:104px;font-family:"Gelasio",Georgia,serif;font-weight:400;font-size:78px;line-height:80px;color:var(--white);z-index:1}
.entry{position:absolute;left:111px;width:978px;height:440px}
.video{position:absolute;left:0;top:0;width:444px;height:284px}
.play{position:absolute;left:190px;top:110px;width:64px;height:64px}
.quote{position:absolute;left:0;top:311px;width:450px;font-size:15px;line-height:28px;color:var(--body)}
.story{position:absolute;left:488px;top:0;width:490px}
.story h2{font-family:"Gelasio",Georgia,serif;font-weight:400;font-size:43px;line-height:46px;color:var(--ink);margin-top:-10px}
.story p{margin-top:20px;font-size:15.5px;line-height:27.5px;color:var(--body)}
.read-more{position:absolute;left:488px;top:243px;font-size:16px;font-weight:700;color:var(--teal);letter-spacing:.3px;text-decoration:none}
.thumb{position:absolute;top:291px;width:141px;height:112px}
.arrow{position:absolute;top:337px;width:14px;height:22px}
.rule{position:absolute;left:111px;width:978px;height:1px;background:var(--rule)}
.load-more{position:absolute;left:507px;top:3220px;width:187px;height:61px;border:2px solid var(--gold);color:var(--gold);font-size:18px;font-weight:700;text-align:center;line-height:57px;letter-spacing:.5px}
.foot-brand{position:absolute;left:108px;top:3440px;font-family:"Gelasio",Georgia,serif;color:var(--gold);font-size:34px;line-height:1.1;width:280px}
.foot-dot{position:absolute;left:210px;top:3362px;width:50px;height:50px;border-radius:50%;background:var(--gold)}
.foot-head{position:absolute;top:3366px;font-family:"Gelasio",Georgia,serif;font-size:24px;color:var(--ink);font-weight:400}
.foot-about{position:absolute;left:450px;top:3412px;width:370px;font-size:14px;line-height:27.5px}
.contact-line{position:absolute;left:853px;font-size:14px;color:var(--body)}
.contact-line svg{vertical-align:-2px;margin-right:8px}
.search{position:absolute;left:112px;top:3554px;width:298px;height:44px;border:2px solid var(--rule);display:flex}
.search-field{flex:1;position:relative}
.search-btn{width:91px;background:var(--gold);color:var(--white);font-weight:700;font-size:15px;text-align:center;line-height:40px}
.copyright{position:absolute;left:112px;top:3662px;font-size:15px}
.social{position:absolute;top:3661px;width:22px;height:22px;border-radius:3px;background:var(--teal)}
</style>
</head>
<body>

<header>
  <div class="nav-band"></div>
  <svg class="brand-cap" viewBox="0 0 1200 200" aria-hidden="true">
    <path d="M462 125 C480 175 540 196 600 196 C660 196 720 175 738 125 Z" fill="#ffffff"/>
  </svg>
  <div class="brand-dot"></div>
  <div class="brand">Velmoran Gatherings</div>
  <nav>
    <a class="nav-link" style="left:181px">PACKAGES</a>
    <a class="nav-link" style="left:353px">ABOUT</a>
    <a class="nav-link" style="left:794px">WEDDINGS</a>
    <a class="nav-link" style="left:970px">BLOG</a>
  </nav>
</header>

<section class="hero" role="img" aria-label="Beach wedding ceremony photo: couple kissing under a wooden arch draped in white fabric, guests seated on white chairs, sea behind"></section>
<h1 class="hero-title">Featured<br>Weddings</h1>

<!-- Entry 1 -->
<article class="entry" style="top:764px">
  <div class="video" role="img" aria-label="Wedding video still: couple exchanging vows by dark coastal rocks with white drapes" style="background:linear-gradient(135deg,#6b6257,#a89c8c 55%,#4d4a44)">
    <svg class="play" viewBox="0 0 64 64"><circle cx="32" cy="32" r="32" fill="#2a2a2a" opacity=".85"/><path d="M25 19 L46 32 L25 45 Z" fill="#fff"/></svg>
  </div>
  <p class="quote">“Mara was amazing! Incredibly easy to work with and supremely helpful! She also found the most beautiful location that I could have ever dreamt!”</p>
  <div class="story">
    <h2>Nadia &amp; Tomas</h2>
    <p>Nadia &amp; Tomas wanted a simple and beautiful small wedding in a stunning location. They contacted us several months before their vacation to Puerto Rico, asking about planning a small wedding in Puerto Rico. Together we chose the stunning Puerto Hermina, home to a gorgeous beach, lush cliffs, and amazing ruins rumored to be leftover from pirate times. It was the perfect spot!</p>
  </div>
  <a class="read-more">READ MORE</a>
  <svg class="arrow" style="left:493px" viewBox="0 0 14 22"><path d="M11 3 L4 11 L11 19" fill="none" stroke="#666" stroke-width="2"/></svg>
  <div class="thumb" style="left:509px;background:linear-gradient(135deg,#5a5650,#a39e97)" role="img" aria-label="Guests gathered at ceremony"></div>
  <div class="thumb" style="left:662px;background:linear-gradient(135deg,#8a8378,#cfc6bb)" role="img" aria-label="Couple with family by the rocks"></div>
  <div class="thumb" style="left:814px;background:linear-gradient(135deg,#4b5a48,#9b9483)" role="img" aria-label="Couple on the beach"></div>
  <svg class="arrow" style="left:971px" viewBox="0 0 14 22"><path d="M3 3 L10 11 L3 19" fill="none" stroke="#666" stroke-width="2"/></svg>
</article>
<div class="rule" style="top:1216px"></div>

<!-- Entry 2 -->
<article class="entry" style="top:1263px">
  <div class="video" role="img" aria-label="Wedding video still: bride in flowing gown on sandy beach with ceremony setup behind" style="background:linear-gradient(180deg,#3d3f2e,#8b7a62 45%,#b7a58c)">
    <svg class="play" viewBox="0 0 64 64"><circle cx="32" cy="32" r="32" fill="#2a2a2a" opacity=".85"/><path d="M25 19 L46 32 L25 45 Z" fill="#fff"/></svg>
  </div>
  <p class="quote">“Mara was amazing! Incredibly easy to work with and supremely helpful! She also found the most beautiful location that I could have ever dreamt!”</p>
  <div class="story">
    <h2>Rhea &amp; Darnell</h2>
    <p>You can tell from their wedding video that Rhea &amp; Darnell have a unique sense of style. When they decided to look for a wedding planner in Puerto Rico, they knew they needed someone they could trust to execute their vision for one of the most important days of their lives. They called Velmoran Gatherings, Inc. and we had a great time making their dreams a reality.</p>
  </div>
  <a class="read-more">READ MORE</a>
  <svg class="arrow" style="left:493px" viewBox="0 0 14 22"><path d="M11 3 L4 11 L11 19" fill="none" stroke="#666" stroke-width="2"/></svg>
  <div class="thumb" style="left:509px;background:linear-gradient(180deg,#8da3b3,#5a4e44)" role="img" aria-label="Couple at dusk on the shore"></div>
  <div class="thumb" style="left:662px;background:linear-gradient(180deg,#4a4232,#c2a17a)" role="img" aria-label="Bride walking on the beach"></div>
  <div class="thumb" style="left:814px;background:linear-gradient(135deg,#2c2420,#b08c6c)" role="img" aria-label="Bride portrait at sunset"></div>
  <svg class="arrow" style="left:971px" viewBox="0 0 14 22"><path d="M3 3 L10 11 L3 19" fill="none" stroke="#666" stroke-width="2"/></svg>
</article>
<div class="rule" style="top:1715px"></div>

<!-- Entry 3 -->
<article class="entry" style="top:1760px">
  <div class="video" role="img" aria-label="Wedding video still: groom in dress uniform at beach ceremony with guests" style="background:linear-gradient(135deg,#d9d2cb,#8e8a85 50%,#2b2d38)">
    <svg class="play" viewBox="0 0 64 64"><circle cx="32" cy="32" r="32" fill="#2a2a2a" opacity=".85"/><path d="M25 19 L46 32 L25 45 Z" fill="#fff"/></svg>
  </div>
  <p class="quote">“Mara was amazing! Incredibly easy to work with and supremely helpful! She also found the most beautiful location that I could have ever dreamt!”</p>
  <div class="story">
    <h2>Ivy &amp; Cole</h2>
    <p>We are grateful to all the essential workers who put themselves at risk to ensure our safety and health. In these unprecedented times, some among us have risen to the challenge of continuing work in the face of danger. In tribute, we are sharing the romantic video of Ivy &amp; Cole’s beach wedding at The Ruins.</p>
  </div>
  <a class="read-more">READ MORE</a>
  <svg class="arrow" style="left:493px" viewBox="0 0 14 22"><path d="M11 3 L4 11 L11 19" fill="none" stroke="#666" stroke-width="2"/></svg>
  <div class="thumb" style="left:509px;background:linear-gradient(180deg,#c9c6c2,#6f6a66)" role="img" aria-label="Couple at the arch"></div>
  <div class="thumb" style="left:662px;background:linear-gradient(180deg,#cfcac4,#2f3140)" role="img" aria-label="Couple smiling together"></div>
  <div class="thumb" style="left:814px;background:linear-gradient(135deg,#e3e1dc,#33343d)" role="img" aria-label="Ceremony moment"></div>
  <svg class="arrow" style="left:971px" viewBox="0 0 14 22"><path d="M3 3 L10 11 L3 19" fill="none" stroke="#666" stroke-width="2"/></svg>
</article>
<div class="rule" style="top:2212px"></div>

<!-- Entry 4 -->
<article class="entry" style="top:2266px">
  <div class="video" role="img" aria-label="Wedding video still: elopement ceremony in a circle of pampas grass on the beach" style="background:linear-gradient(180deg,#bfc4c4,#d8ccb8 55%,#b59c80)">
    <svg class="play" viewBox="0 0 64 64"><circle cx="32" cy="32" r="32" fill="#2a2a2a" opacity=".85"/><path d="M25 19 L46 32 L25 45 Z" fill="#fff"/></svg>
  </div>
  <p class="quote">“Mara was amazing! Incredibly easy to work with and supremely helpful! She also found the most beautiful location that I could have ever dreamt!”</p>
  <div class="story">
    <h2>Marisol &amp; Andres Elope</h2>
    <p>We love the subtle color palette of Marisol &amp; Andres’ adventure elopement. They were married in a circle of pampas grass at Swallow’s Pool in Isabela. Pampas grass is on-trend in the wedding industry and we love the unique feel that this setting creates. We are fortunate that pampas grass grows wild in many places in Puerto Rico.</p>
  </div>
  <a class="read-more">READ MORE</a>
  <svg class="arrow" style="left:493px" viewBox="0 0 14 22"><path d="M11 3 L4 11 L11 19" fill="none" stroke="#666" stroke-width="2"/></svg>
  <div class="thumb" style="left:509px;background:linear-gradient(180deg,#c7d0d3,#d8cdbd)" role="img" aria-label="Groom in light suit by the sea"></div>
  <div class="thumb" style="left:662px;background:linear-gradient(180deg,#c9ad8c,#9c7c5c)" role="img" aria-label="Pampas circle from above"></div>
  <div class="thumb" style="left:814px;background:linear-gradient(180deg,#c6c9c8,#b89772)" role="img" aria-label="Couple on the coastline"></div>
  <svg class="arrow" style="left:971px" viewBox="0 0 14 22"><path d="M3 3 L10 11 L3 19" fill="none" stroke="#666" stroke-width="2"/></svg>
</article>
<div class="rule" style="top:2718px"></div>

<!-- Entry 5 -->
<article class="entry" style="top:2763px">
  <div class="video" role="img" aria-label="Wedding video still: aerial view of a ceremony on a palm-lined sandy beach" style="background:linear-gradient(180deg,#3c4231,#8d7c63 40%,#b19a7e)">
    <svg class="play" viewBox="0 0 64 64"><circle cx="32" cy="32" r="32" fill="#2a2a2a" opacity=".85"/><path d="M25 19 L46 32 L25 45 Z" fill="#fff"/></svg>
  </div>
  <p class="quote">“Mara was amazing! Incredibly easy to work with and supremely helpful! She also found the most beautiful location that I could have ever dreamt!”</p>
  <div class="story">
    <h2>Elena &amp; Marco</h2>
    <p>Most of our weddings are destination weddings (hence our name) but sometimes the destination is home as well! This was true for Elena, who lives in Texas but has a big, beautiful family in Puerto Rico. Her groom-to-be, Marco, proposed to her at Christmastime in 2018 when they were in Puerto Rico, in front of her whole family (bold move, but it worked!).</p>
  </div>
  <a class="read-more">READ MORE</a>
  <svg class="arrow" style="left:493px" viewBox="0 0 14 22"><path d="M11 3 L4 11 L11 19" fill="none" stroke="#666" stroke-width="2"/></svg>
  <div class="thumb" style="left:509px;background:linear-gradient(180deg,#9aa3a8,#4a3a2c)" role="img" aria-label="Ceremony arch on the beach"></div>
  <div class="thumb" style="left:662px;background:linear-gradient(135deg,#2e3a55,#d8cfc6)" role="img" aria-label="Bride portrait"></div>
  <div class="thumb" style="left:814px;background:linear-gradient(180deg,#e6e3de,#8f9570)" role="img" aria-label="Couple walking hand in hand"></div>
  <svg class="arrow" style="left:971px" viewBox="0 0 14 22"><path d="M3 3 L10 11 L3 19" fill="none" stroke="#666" stroke-width="2"/></svg>
</article>

<div class="load-more">LOAD MORE</div>

<div class="rule" style="top:3321px"></div>

<footer>
  <div class="foot-dot"></div>
  <div class="foot-brand">Velmoran Gatherings</div>

  <h3 class="foot-head" style="left:450px">About</h3>
  <p class="foot-about">Velmoran Gatherings, Inc. is owned and operated by Mara Ellison, a non-denominational minister who became ordained to perform weddings, and has extensive experience planning and coordinating hundreds of weddings on our enchanted island. She will be your point of contact at every step.</p>

  <h3 class="foot-head" style="left:853px">Contact</h3>
  <div class="contact-line" style="top:3421px">
    <svg width="14" height="14" viewBox="0 0 14 14"><path d="M3 1 L5.5 1 L6.5 4 L5 5.5 C6 7.5 7 8.5 8.5 9 L10 7.5 L13 8.5 L13 11 C13 12 12 13 11 13 C5.5 12.5 1.5 8.5 1 3 C1 2 2 1 3 1 Z" fill="#dfbd78"/></svg>555.014.2273
  </div>
  <div class="contact-line" style="top:3476px">
    <svg width="16" height="12" viewBox="0 0 16 12"><rect x="0" y="0" width="16" height="12" rx="1" fill="#dfbd78"/><path d="M1 1 L8 7 L15 1" fill="none" stroke="#fff" stroke-width="1.4"/></svg>info@velmorangatherings.com
  </div>

  <div class="search">
    <div class="search-field">
      <svg style="position:absolute;left:11px;top:12px" width="16" height="16" viewBox="0 0 16 16"><circle cx="6.5" cy="6.5" r="5" fill="none" stroke="#999" stroke-width="1.6"/><path d="M10.5 10.5 L15 15" stroke="#999" stroke-width="1.6"/></svg>
    </div>
    <div class="search-btn">SEARCH</div>
  </div>

  <div class="rule" style="top:3633px"></div>
  <p class="copyright">© 2020, Velmoran Gatherings.</p>
  <span class="social" style="left:964px" aria-label="Social link"></span>
  <span class="social" style="left:998px" aria-label="Social link"></span>
  <span class="social" style="left:1032px" aria-label="Social link"></span>
  <span class="social" style="left:1066px" aria-label="Social link"></span>
</footer>

</body>
</html>
```